I need a new design for my real estate signage!

Would like a new design for my real estate signs. I do have a logo that needs to be used along with the word AVAILABLE and my phone number 505-718-2094

Target Market(s)

Real estate buyers and sellers

Industry/Entity Type

Real Estate

Font styles to use
Serif

Colors
000000

Requirements
Must have
• Company name phone number
• Colors: turquoise, white black
Nice to have
• Modern design

```html
<!DOCTYPE html>
<html lang="en">
<head>
<meta charset="utf-8">
<title>Corvell Real Estate Services – Available Sign</title>
<link rel="stylesheet" href="https://fonts.googleapis.com/css2?family=Bebas+Neue&family=Cinzel:wght@500&display=swap">
<style>
  :root {
    --sign-black: #000000;
    --sign-white: #ffffff;
    --teal: #17808c;
    --teal-dark: #0d5d66;
    --teal-light: #1c9aa6;
  }
  html, body {
    margin: 0;
    padding: 0;
    width: 1200px;
    height: 900px;
    overflow: hidden;
    background: var(--sign-black);
  }
  .sign {
    position: relative;
    width: 1200px;
    height: 900px;
    background: var(--sign-black);
    overflow: hidden;
  }
  .corner-ribbons {
    position: absolute;
    inset: 0;
    width: 1200px;
    height: 900px;
  }
  .brand {
    position: absolute;
    left: 400px;
    top: 118px;
    display: flex;
    align-items: center;
    gap: 26px;
    color: var(--teal);
    font-family: "Cinzel", serif;
    font-weight: 500;
  }
  .brand-square {
    width: 78px;
    height: 78px;
    background: var(--teal);
  }
  .brand-name {
    display: flex;
    flex-direction: column;
  }
  .brand-title {
    font-size: 78px;
    line-height: 1;
    letter-spacing: 0.01em;
  }
  .brand-tagline {
    font-size: 19px;
    letter-spacing: 0.36em;
    margin-top: 6px;
  }
  .headline {
    position: absolute;
    left: 178px;
    top: 320px;
    width: 842px;
    margin: 0;
    font-family: "Bebas Neue", sans-serif;
    font-weight: 400;
    font-size: 226px;
    line-height: 1;
    letter-spacing: 0.035em;
    color: var(--sign-white);
    text-align: center;
    white-space: nowrap;
  }
  .divider {
    position: absolute;
    left: 178px;
    top: 525px;
    width: 842px;
    height: 8px;
    background: var(--teal);
  }
  .phone {
    position: absolute;
    left: 178px;
    top: 548px;
    width: 842px;
    margin: 0;
    font-family: "Bebas Neue", sans-serif;
    font-size: 114px;
    line-height: 1;
    letter-spacing: 0.05em;
    color: var(--sign-white);
    text-align: center;
    white-space: nowrap;
  }
</style>
</head>
<body>
  <main class="sign">
    <svg class="corner-ribbons" viewBox="0 0 1024 768" preserveAspectRatio="none" aria-hidden="true">
      <polygon points="718,0 1024,0 1024,178 878,102 878,45" fill="var(--teal)"/>
      <polygon points="878,45 1024,84 1024,178 878,102" fill="var(--teal-dark)"/>
      <polygon points="0,578 156,657 156,720 330,768 0,768" fill="var(--teal)"/>
      <polygon points="0,660 156,657 156,720 0,705" fill="var(--teal-dark)"/>
    </svg>

    <div class="brand">
      <div class="brand-square"></div>
      <div class="brand-name">
        <span class="brand-title">CORVELL</span>
        <span class="brand-tagline">REAL ESTATE SERVICES</span>
      </div>
    </div>

    <h1 class="headline">AVAILABLE</h1>
    <div class="divider"></div>
    <p class="phone">CALL: 505-718-2094</p>
  </main>
</body>
</html>
```